Retail Sign for Houseplant Campaign

Sign will measure 3 to 4 foot tall by 22.2inches and place on rolling racks of houseplants for a retail promotion in The Yardwell Mart. The theme of the promotion will be "New Year, New You!" Selling points which should be on the sign are Houseplants give you a taste of nature, Houseplants boost air quality inside your home, Indoor plants reduce anxiety, Indoor plants make you more productive, Houseplants improve your concentration and memory.
Updates

Target Market(s)

People who love plants

Industry/Entity Type

Horticulture/ retail

Colors
00AB8E
00BBA5
67D7C9
C6EFE9
E9F9F6
59FF00
82FF00
B8FF75
E3FFCB
F4FFEA
FFF300
FFF600
FEFA6F
FFFEC7
FFFEE8

Requirements
Must have
• Must feel energetic and encourage people to buy plants. Should include 1-2 photos and the selling points listed

```html
<!DOCTYPE html>
<html lang="en">
<head>
<meta charset="utf-8">
<title>New Year, New You – Houseplant Sign</title>
<link href="https://fonts.googleapis.com/css2?family=Kaushan+Script&family=Montserrat:wght@400;600;700&display=swap" rel="stylesheet">
<style>
  :root {
    --backdrop: #e4e4e4;
    --paper: #ffffff;
    --sun: #f9ee6b;
    --leaf-dark: #3d5a2a;
    --ink-white: #ffffff;
  }
  * { margin: 0; padding: 0; box-sizing: border-box; }
  html, body { width: 1200px; height: 1165px; overflow: hidden; background: var(--backdrop); }
  .stage { position: relative; width: 1200px; height: 1165px; }
  .sign {
    position: absolute; left: 346px; top: 30px;
    width: 609px; height: 1327px;
    transform: scale(0.8327); transform-origin: 0 0;
    background: var(--paper);
    overflow: hidden;
    font-family: "Montserrat", sans-serif;
  }
  .sign-art { position: absolute; inset: 0; width: 609px; height: 1327px; }
  .store-name {
    position: absolute; left: 40px; top: 52px; width: 160px;
    display: flex; align-items: center; gap: 10px;
  }
  .store-name .mark { width: 24px; height: 24px; border-radius: 50%; background: var(--leaf-dark); flex: none; }
  .store-name span {
    font-weight: 700; font-size: 18px; line-height: 1.15; color: var(--leaf-dark);
  }
  .headline { position: absolute; inset: 0; font-family: "Kaushan Script", cursive; font-weight: 400; pointer-events: none; }
  .headline span { position: absolute; line-height: 1; white-space: nowrap; }
  .hl-new-big { left: 100px; top: 560px; font-size: 112px; color: var(--ink-white); transform: rotate(-4deg); }
  .hl-year { left: 312px; top: 628px; font-size: 46px; color: var(--leaf-dark); transform: rotate(-4deg); }
  .hl-new-small { left: 132px; top: 686px; font-size: 48px; color: var(--leaf-dark); transform: rotate(-4deg); }
  .hl-you { left: 236px; top: 664px; font-size: 116px; color: var(--ink-white); transform: rotate(-4deg); }
  .hl-bang { left: 446px; top: 560px; font-size: 190px; color: var(--ink-white); transform: rotate(6deg); }
  .benefits { position: absolute; left: 50px; top: 808px; color: var(--leaf-dark); }
  .benefits h2 { font-weight: 700; font-size: 39px; line-height: 1; margin-bottom: 12px; }
  .benefits ul { list-style: none; }
  .benefits li {
    display: flex; align-items: center; gap: 20px;
    font-weight: 600; font-size: 24.5px; height: 39px; white-space: nowrap;
  }
  .benefits li::before {
    content: ""; width: 26px; height: 26px; border-radius: 50%;
    background: var(--ink-white); flex: none;
  }
  .maker { position: absolute; left: 124px; top: 1222px; display: flex; align-items: center; gap: 18px; color: var(--leaf-dark); }
  .maker .mark { width: 74px; height: 72px; background: var(--leaf-dark); }
  .maker .name { font-weight: 400; line-height: 1; }
  .maker .name strong { display: block; font-weight: 400; font-size: 50px; letter-spacing: 0.5px; }
  .maker .name small { display: block; font-size: 19px; letter-spacing: 10px; margin-top: 6px; }
</style>
</head>
<body>
<main class="stage">
  <section class="sign" aria-label="New Year, New You houseplant sign">
    <svg class="sign-art" viewBox="0 0 609 1327">
      <defs>
        <linearGradient id="yellow-field" x1="0" y1="0" x2="0" y2="1">
          <stop offset="0" stop-color="#f7ea55"/>
          <stop offset="1" stop-color="#fbf27e"/>
        </linearGradient>
        <linearGradient id="photo-family" x1="0" y1="0" x2="1" y2="1">
          <stop offset="0" stop-color="#e9e4df"/>
          <stop offset="0.5" stop-color="#a7b0b5"/>
          <stop offset="1" stop-color="#4f6a46"/>
        </linearGradient>
        <linearGradient id="photo-shelf" x1="0" y1="0" x2="1" y2="1">
          <stop offset="0" stop-color="#eef0ee"/>
          <stop offset="0.6" stop-color="#d2b497"/>
          <stop offset="1" stop-color="#8c7b6b"/>
        </linearGradient>
        <linearGradient id="photo-leaf" x1="0" y1="0" x2="1" y2="1">
          <stop offset="0" stop-color="#eeeeee"/>
          <stop offset="1" stop-color="#3f7a36"/>
        </linearGradient>
      </defs>
      <path class="yellow-field" d="M0 250 C60 215 150 200 230 190 L609 150 L609 1070 C520 1140 390 1175 270 1168 C160 1160 70 1125 0 1082 Z" fill="url(#yellow-field)"/>
      <path class="bottom-swoosh" d="M0 1078 C90 1140 200 1176 300 1180 C410 1184 520 1140 609 1068" fill="none" stroke="var(--leaf-dark)" stroke-width="13"/>
      <path role="img" aria-label="Photo: mother and daughter watering a snake plant" d="M215 0 L609 0 L609 398 C520 418 420 410 330 390 C260 330 215 200 215 0 Z" fill="url(#photo-family)"/>
      <path class="photo-edge" d="M205 0 C198 140 212 220 240 258" fill="none" stroke="var(--leaf-dark)" stroke-width="9"/>
      <ellipse role="img" aria-label="Monstera leaf decoration" cx="105" cy="222" rx="82" ry="58" transform="rotate(-20 105 222)" fill="var(--leaf-dark)"/>
      <ellipse role="img" aria-label="Monstera leaf decoration" cx="530" cy="1112" rx="62" ry="48" transform="rotate(-25 530 1112)" fill="var(--leaf-dark)"/>
      <circle role="img" aria-label="Photo: woman arranging a potted croton" cx="196" cy="409" r="150" fill="url(#photo-shelf)" stroke="#fff" stroke-width="6"/>
      <circle role="img" aria-label="Photo: woman wiping a monstera leaf" cx="427" cy="409" r="97" fill="url(#photo-leaf)" stroke="#fff" stroke-width="6"/>
    </svg>

    <div class="store-name"><i class="mark"></i><span>The Yardwell Mart</span></div>

    <h1 class="headline" aria-label="New Year, New You!">
      <span class="hl-new-big">New</span>
      <span class="hl-year">Year,</span>
      <span class="hl-new-small">New</span>
      <span class="hl-you">You</span>
      <span class="hl-bang">!</span>
    </h1>

    <div class="benefits">
      <h2>Houseplants</h2>
      <ul>
        <li>Give You a Taste of Nature</li>
        <li>Improve Indoor Air Quality</li>
        <li>Reduce Anxiety</li>
        <li>Make You Productive</li>
        <li>Improve Concentration &amp; Memory</li>
      </ul>
    </div>

    <div class="maker">
      <i class="mark"></i>
      <p class="name"><strong>VERDALE</strong><small>GREENHOUSE</small></p>
    </div>
  </section>
</main>
</body>
</html>
```